An e-flyer for an exotic car and fine wine club.

This is the first meeting of Birchwell Motor Society and includes several businesses. Their logos should be featured at the bottom. It should be sleek, elegant and simple featuring a photo of an Corvane Lestrel R7 as well as my logo (I will provide photos). The flyer needs to look professional and appeal to billionaires.
The text should read:
Birchwell Motor society presents
Fast Cars and Fine Wine (but not while driving)
Hosted by Harlow Gem Vault
Bring your best car(s) and join us to enjoy the party with sommelier selected wines, the best classic and modern cars and hors d'oeuvre catered by Penrose's Clam House. Live DJ.
August 26th 3-6 p.m.
This event is gratis.
RSVP to dana@birchwellmotors.example for address and details

Target Market(s)
Very wealthy exotic car owners
Industry/Entity Type
Car Club, Fine Wines.
Requirements
Must have
- Style, panache, elegance, sleekness, simplicity. I like the idea of a black or dark flyer with a consistent color scheme.
Nice to have
- I want the flyer to be simple and sleek, feature an Corvane Lestrel R7 as the eye catcher, Birchwell Motor Society logo featured prominently on the top, and the other business logos on the bottom.
Should not have
- It must not be too noisy or busy.

```html
<!DOCTYPE html>
<html lang="en">
<head>
<meta charset="utf-8">
<title>Fast Cars and Fine Wine — Birchwell Motor Society</title>
<link href="https://fonts.googleapis.com/css2?family=Bebas+Neue&family=Lexend:wght@400;500;600;700&display=swap" rel="stylesheet">
<style>
  :root {
    --night: #0f1a3d;
    --dusk: #24355f;
    --haze: #7d8aa8;
    --ground: #3a3630;
    --paint: #8e1a22;
    --paint-dark: #4a0c12;
    --ink: #ffffff;
    --pill: #000000;
  }
  * { margin: 0; padding: 0; box-sizing: border-box; }
  html, body { width: 848px; height: 1200px; overflow: hidden; background: var(--night); }
  .flyer {
    position: relative;
    width: 848px;
    height: 1200px;
    overflow: hidden;
    color: var(--ink);
    font-family: "Lexend", sans-serif;
    text-align: center;
  }
  .backdrop {
    position: absolute; inset: 0;
    background: linear-gradient(180deg, #0c163a 0%, var(--night) 28%, var(--dusk) 45%, #2b3c66 60%, var(--haze) 72%, #5b6479 80%, var(--ground) 92%, #24211d 100%);
  }
  .car-photo {
    position: absolute;
    left: 24px; top: 773px;
    width: 800px; height: 330px;
    border-radius: 46% 50% 12% 12% / 60% 60% 14% 14%;
    background: radial-gradient(ellipse at 55% 40%, #b2323a 0%, var(--paint) 45%, var(--paint-dark) 100%);
  }
  .content { position: relative; }
  .club-name {
    position: absolute; left: 0; right: 0; top: 78px;
    font-weight: 600;
    line-height: 1.1;
  }
  .club-name .mark {
    display: inline-block; width: 18px; height: 18px;
    border-radius: 50%; background: var(--ink);
    margin-bottom: 14px;
  }
  .club-name .word { display: block; font-size: 46px; letter-spacing: 4px; }
  .club-name .sub { display: block; font-size: 23px; letter-spacing: 13px; margin-top: 6px; }
  .presents {
    position: absolute; left: 0; right: 0; top: 256px;
    font-size: 20px; font-weight: 500; letter-spacing: 5px; text-transform: uppercase;
  }
  .title {
    position: absolute; left: 0; right: 0; top: 282px;
    font-family: "Bebas Neue", sans-serif;
    font-size: 82px; font-weight: 400; line-height: 1; letter-spacing: 1px;
  }
  .aside {
    position: absolute; left: 0; right: 0; top: 360px;
    font-size: 31px; font-weight: 700;
  }
  .host {
    position: absolute; left: 0; right: 0; top: 421px;
    font-size: 21px; font-weight: 600;
  }
  .details {
    position: absolute; left: 80px; right: 80px; top: 474px;
    font-size: 21px; font-weight: 400; line-height: 28.5px;
  }
  .date {
    position: absolute; left: 0; right: 0; top: 586px;
    font-size: 29px; font-weight: 700;
  }
  .price {
    position: absolute; left: 295px; top: 634px;
    width: 258px; height: 47px; border-radius: 24px;
    background: var(--pill);
    font-size: 21px; font-weight: 500; line-height: 47px;
  }
  .rsvp {
    position: absolute; left: 0; right: 0; top: 700px;
    font-size: 19px; font-weight: 600;
  }
  .partners {
    position: absolute; left: 0; right: 0; top: 1138px;
    display: flex; justify-content: center; gap: 44px;
    font-size: 17px; font-weight: 600; letter-spacing: 1px;
  }
</style>
</head>
<body>
<main class="flyer">
  <div class="backdrop" role="img" aria-label="Dusk sky with dark blue clouds over a shoreline"></div>
  <div class="car-photo" role="img" aria-label="Red Corvane Lestrel R7 classic coupe parked on gravel by the sea"></div>

  <section class="content">
    <div class="club-name">
      <span class="mark"></span>
      <span class="word">BIRCHWELL</span>
      <span class="sub">MOTOR SOCIETY</span>
    </div>
    <p class="presents">Birchwell Motor Society presents</p>
    <h1 class="title">Fast Cars and Fine Wine</h1>
    <p class="aside">(but not while driving)</p>
    <p class="host">Hosted by Harlow Gem Vault</p>
    <p class="details">Bring your best car(s) and join us to enjoy the party with sommelier selected wines, the best classic and modern cars and hors d'oeuvre catered by Penrose's Clam House. Live DJ.</p>
    <p class="date">August 26th 3-6 p.m.</p>
    <p class="price">This event is gratis.</p>
    <p class="rsvp">RSVP to dana@birchwellmotors.example for address and details</p>
  </section>

  <footer class="partners">
    <span class="partner">Ashby Wine Store</span>
    <span class="partner">Harlow Gem Vault</span>
  </footer>
</main>
</body>
</html>
```